Real Estate Company Needs a Contemporary/Modern Business Card Design

We need a Contemporary/Modern Business Card Design for a New Real Estate Company based in San Francisco, CA called Colvane Terrish Realtors. We would like to see designs that use the color red for the "Colvane Terrish" and gold for the "Realtors." The design should communicate being Modern and yet Established and Stable.

Industry/Entity Type

Business

```html
<!DOCTYPE html>
<html lang="en">
<head>
<meta charset="utf-8">
<title>Colvane Terrish Realtors – Business Card</title>
<link href="https://fonts.googleapis.com/css2?family=Open+Sans:wght@400;600;700&display=swap" rel="stylesheet">
<style>
  :root {
    --backdrop: #c9c9c9;
    --card-white: #ffffff;
    --red-deep: #6e0d12;
    --red-main: #8f161c;
    --red-brand: #c3161f;
    --gold: #d4a92a;
    --gold-light: #f1d479;
    --silver: #e4e4e4;
    --ink-light: #ffffff;
  }
  * { box-sizing: border-box; margin: 0; padding: 0; }
  html, body { width: 1200px; height: 900px; overflow: hidden; }
  body {
    background: var(--backdrop);
    font-family: "Open Sans", Arial, sans-serif;
    position: relative;
  }
  .card {
    position: absolute;
    top: 300px;
    width: 520px;
    height: 300px;
    border-radius: 26px;
    overflow: hidden;
  }
  .card--front { left: 50px; background: var(--card-white); }
  .card--back {
    left: 630px;
    background: radial-gradient(ellipse at 50% 45%, var(--red-main) 0%, var(--red-deep) 100%);
  }
  .wordmark {
    position: absolute;
    left: 0; right: 0;
    text-align: center;
    font-weight: 700;
  }
  .wordmark__name {
    display: block;
    font-size: 38px;
    line-height: 44px;
    letter-spacing: 1px;
  }
  .wordmark__trade {
    display: block;
    font-size: 15px;
    line-height: 20px;
    letter-spacing: 16px;
    padding-left: 16px;
    text-transform: uppercase;
    color: var(--gold);
  }
  .card--front .wordmark { top: 40px; }
  .card--front .wordmark__name { color: var(--red-brand); }
  .card--back .wordmark { top: 112px; }
  .card--back .wordmark__name { color: var(--silver); }
  .card--back .wordmark__trade { color: var(--gold-light); }
  .gold-band {
    position: absolute;
    top: 138px; left: 0; right: 0;
    height: 8px;
    background: linear-gradient(90deg, var(--gold) 0%, var(--gold-light) 50%, var(--gold) 100%);
  }
  .contact-panel {
    position: absolute;
    top: 146px; left: 0; right: 0; bottom: 0;
    background: linear-gradient(180deg, var(--red-main) 0%, var(--red-deep) 100%);
    padding: 10px 22px;
    color: var(--ink-light);
  }
  .person-name { color: var(--gold-light); font-weight: 600; font-size: 17px; line-height: 1.2; }
  .person-role { font-size: 10px; margin-bottom: 12px; }
  .contact-list { list-style: none; font-size: 11.5px; line-height: 17px; }
  .contact-list li { display: flex; align-items: center; gap: 6px; }
  .contact-list svg { width: 11px; height: 11px; flex: none; fill: var(--gold-light); }
</style>
</head>
<body>
  <section class="card card--front" aria-label="Business card front">
    <div class="wordmark">
      <span class="wordmark__name">Colvane Terrish</span>
      <span class="wordmark__trade">Realtors</span>
    </div>
    <div class="gold-band"></div>
    <div class="contact-panel">
      <p class="person-name">Colvane Terrish</p>
      <p class="person-role">Manager</p>
      <ul class="contact-list">
        <li><svg viewBox="0 0 12 12"><path d="M2 1h2.5l1 3-1.5 1a6 6 0 0 0 3 3l1-1.5 3 1V10a1 1 0 0 1-1 1A9 9 0 0 1 1 2a1 1 0 0 1 1-1z"/></svg>415-555-0142</li>
        <li><svg viewBox="0 0 12 12"><rect x="1" y="4" width="10" height="6" rx="1"/><rect x="3" y="1" width="6" height="3"/></svg>415-555-0178</li>
        <li><svg viewBox="0 0 12 12"><path d="M1 3h10v7H1z M1 3l5 4 5-4" stroke="#6e0d12" stroke-width=".8"/></svg>info@colvaneterrishrealtors.com</li>
        <li><svg viewBox="0 0 12 12"><circle cx="6" cy="6" r="5"/></svg>www.colvaneterrishrealtors.com</li>
        <li><svg viewBox="0 0 12 12"><path d="M6 1l5 5H9.5v5h-7V6H1z"/></svg>214 Larkin st San Francisco CA 94102</li>
      </ul>
    </div>
  </section>

  <section class="card card--back" aria-label="Business card back">
    <div class="wordmark">
      <span class="wordmark__name">Colvane Terrish</span>
      <span class="wordmark__trade">Realtors</span>
    </div>
  </section>
</body>
</html>
```